Flyer Design for a Boston Therapeutic Clinic

I am a body therapist who needs a couple of flyers designed:
1. To fit half a page.
2. To fit a 5 inch by 3.5 inch flyer.
My practice is based in Boston, MA and my web site is:
www.LarchTessvik.Com
For the First half page:
A. Have my company's name and color shown as it appears on my web site (Larch Tessvik)
B. Have the following text: "Control your weight (This part should be emphasized) by balancing your nervous and digestive system through the Tessvik Method. The Tessvik Method, a technique developed by Dr. Mara. Tessvik, uses physical pressure to manipulate visceral tissue to bring back resiliency and proper functioning of the whole body."
Also helps with
-Constipation
-Bloating
-IBS
-eating disorders and overeating
Our practitioner is highly experienced. Please visit our web sites for reviews.
C. I would like to have a nice earthy feeling, something that feels "freeing" like open flowers, or an open land scape such as mountains or fields.
D. I also like the color blue, white, orange; perhaps if these colors can be integrated into the flyer, that would be great.
E. "Visit our web site LarchTessvik.com or call 786-555-0148"
The Smaller Flyer :
A.The smaller Flyer should also have my Company's name as shown on my web site (Larch Tessvik)
B.The following text: " Restore your body's natural resiliency and greatly reduce your physical pain through the Dr. Mara Tessvik Method of Structural Integration."
C. "Our practitioner is highly experienced and has a great reputation; visit our web site for reviews."
"Benefits:
"reduce aches and pains
reduce joint pain
reduce chronic muscular tension"
D, "feel better after the first session!"
E. if you could use a picture of me working on someone from my web site, that would be great.
F. I also like the colors white, orange and silver, for this one.
G. "Visit our web site LarchTessvik.com or call 786-555 0148"
I am very open minded,
I would like the flyer to evoke a sense of tranquility, professionalism, and simplicity. So if you have another angle you think would look good, then go for it! As long as it looks clean, professional and helpful.
Thanks a lot!
If you need any pictures from my web site, I have the original high resolution files that i can send.
Professionals and working men and women from ages 20-70
Clinic

```html
<!DOCTYPE html>
<html lang="en">
<head>
<meta charset="utf-8">
<title>Larch Tessvik Therapy – Flyer</title>
<link rel="stylesheet" href="https://fonts.googleapis.com/css2?family=Didact+Gothic&family=Montserrat:wght@700&display=swap">
<style>
  :root {
    --brand-orange: #e4572e;
    --ink-grey: #5a5a5a;
    --title-grey: #5e5e5e;
    --paper: #ffffff;
    --sky-pale: #dcebf6;
    --sky-mid: #9cc8ea;
    --sky-deep: #5fa2d8;
    --cloud: #eef1f3;
    --mountain: #41648e;
    --field-orange: #c9773a;
    --field-dark: #8a4a22;
  }
  * { margin: 0; padding: 0; box-sizing: border-box; }
  html, body { width: 851px; height: 1200px; overflow: hidden; background: var(--paper); }
  .flyer {
    position: relative;
    width: 851px;
    height: 1200px;
    overflow: hidden;
    background: var(--paper);
    font-family: "Didact Gothic", "Century Gothic", sans-serif;
    color: var(--ink-grey);
  }
  .landscape {
    position: absolute;
    left: 0; top: 450px;
    width: 851px; height: 750px;
    background: linear-gradient(180deg,
      rgba(255,255,255,0) 0%,
      var(--sky-pale) 12%,
      var(--sky-mid) 24%,
      var(--sky-deep) 36%,
      #84b6de 42%,
      var(--cloud) 46%,
      #b9c8d6 49%,
      var(--mountain) 53%,
      #5a6b70 57%,
      #a8743f 61%,
      var(--field-orange) 72%,
      var(--field-orange) 86%,
      var(--field-dark) 100%);
  }
  .brand {
    position: absolute;
    top: 86px; left: 0; width: 851px;
    text-align: center;
    font-family: "Didact Gothic", sans-serif;
    font-weight: 400;
    font-size: 54px;
    line-height: 1;
    color: var(--title-grey);
    white-space: nowrap;
  }
  .pitch {
    position: absolute;
    top: 180px; left: 72px; width: 704px;
  }
  .pitch-line {
    display: flex;
    justify-content: space-between;
    align-items: baseline;
    gap: 10px;
    white-space: nowrap;
    height: 47px;
    color: var(--ink-grey);
  }
  .pitch-line.right { justify-content: flex-end; height: 42px; }
  .big { font-size: 48px; }
  .mid { font-size: 38px; }
  .small { font-size: 26px; }
  .method-tag {
    font-family: "Montserrat", sans-serif;
    font-weight: 700;
    font-size: 19px;
    color: var(--brand-orange);
  }
  .details {
    position: absolute;
    top: 536px; left: 74px;
    display: flex;
  }
  .practitioner {
    width: 262px;
    font-size: 22px;
    line-height: 38px;
  }
  .divider {
    width: 2px;
    height: 146px;
    margin: 6px 30px 0 8px;
    background: var(--ink-grey);
  }
  .helps-title {
    font-family: "Montserrat", sans-serif;
    font-weight: 700;
    font-size: 19px;
    color: #4d4d4d;
    margin-bottom: 4px;
  }
  .helps-list { list-style: none; font-size: 22px; line-height: 29px; }
  .helps-list li::before { content: "\2022\00a0"; }
  .contact {
    position: absolute;
    top: 1113px; left: 0; width: 851px;
    text-align: center;
    font-size: 19px;
    color: var(--paper);
  }
  .contact strong { font-family: "Montserrat", sans-serif; font-weight: 700; }
</style>
</head>
<body>
<main class="flyer">
  <div class="landscape" role="img" aria-label="Open landscape photograph: blue sky with clouds over distant mountains and a wide field of golden-orange grass"></div>

  <h1 class="brand">Larch Tessvik Therapy</h1>

  <section class="pitch">
    <div class="pitch-line"><span class="big">Control your weight</span><span class="small">by balancing</span></div>
    <div class="pitch-line"><span class="small">your nervous and digestive system</span><span class="big">through</span></div>
    <div class="pitch-line"><span class="mid">the Tessvik Method.</span><span class="method-tag">The Tessvik Method technique</span></div>
    <div class="pitch-line right"><span class="small">developed by Dr. Mara. Tessvik, uses</span></div>
    <div class="pitch-line"><span class="big">physical pressure</span><span class="small">to manipulate visceral</span></div>
    <div class="pitch-line"><span class="small">tissue to</span><span class="big">bring back resiliency</span><span class="small">and</span></div>
    <div class="pitch-line"><span class="big">proper functioning</span><span class="small">of the whole body.</span></div>
  </section>

  <section class="details">
    <p class="practitioner">Our practitioner is highly experienced. Please visit our web sites for reviews.</p>
    <div class="divider"></div>
    <div class="helps">
      <h2 class="helps-title">Also helps with:</h2>
      <ul class="helps-list">
        <li>Constipation</li>
        <li>Bloating</li>
        <li>IBS</li>
        <li>Eating Disorders and Overeating</li>
      </ul>
    </div>
  </section>

  <p class="contact">Visit our website on <strong>www.LarchTessvik.com</strong> or call <strong>786-555-0148</strong></p>
</main>
</body>
</html>
```